Love Your Hearing - Life Sounds Good

I need a website. I had a company doing it, and it looked very nice, but they went way up on hosting costs and said they owned the design of the site. I changed hosts to keep costs down. You can see the current design at crestvaleaudio.com. They said I could use the copy and images from the current website. So you could cut and paste to speed things up. My logo and other images are on the current website. If you are unable to use I can send other digital copies.

Target Market(s)

seniors 55 and up

Number of Pages Required

4 page

Font styles to use
Sans Serif

Colors
0255a3
f78f20

Requirements
Must have
• Video testimonies that I can add without assistance. I use youtube links for the videos.
Nice to have
• The color scheme theme can be drawn from the logo, which is on the current webstie crestvaleaudio.com
Should not have
• Should not have anything related to SonoPath on the website.

```html
<!DOCTYPE html>
<html lang="en">
<head>
<meta charset="utf-8">
<title>Crestvale Audio – Love Your Hearing</title>
<link rel="stylesheet" href="https://fonts.googleapis.com/css2?family=Merriweather:wght@400;700&family=Open+Sans:wght@400;600;700&display=swap">
<style>
:root{
  --blue:#0255a3;
  --blue-dark:#013f7d;
  --orange:#f78f20;
  --ink:#333;
  --muted:#666;
  --line:#e2e2e2;
  --footer:#2b2b2b;
  --footer-bottom:#1f1f1f;
  --white:#fff;
}
*{box-sizing:border-box;margin:0;padding:0}
html,body{width:1200px;height:3128px;overflow:hidden}
body{font-family:"Open Sans",Arial,sans-serif;color:var(--ink);background:var(--white);position:relative}
.serif{font-family:"Merriweather",Georgia,serif}
.abs{position:absolute}
.btn{display:inline-block;background:var(--orange);color:var(--white);font-size:14px;font-weight:600;padding:8px 26px;border-radius:3px}

/* header */
.topbar{position:absolute;top:0;left:0;width:1200px;height:112px}
.brand{position:absolute;left:72px;top:22px;display:flex;align-items:center;gap:12px}
.brand-dot{width:62px;height:62px;border-radius:50%;background:var(--orange)}
.brand-name{font-size:30px;font-weight:700;color:var(--blue);line-height:1}
.contact-strip{position:absolute;right:80px;top:34px;display:flex;align-items:center;gap:22px;font-size:13px;color:var(--muted)}
.contact-item{display:flex;align-items:center;gap:8px;line-height:1.3}
.socials{display:flex;gap:8px}
.socials span{width:22px;height:22px;border-radius:50%;background:var(--orange)}
.socials span:nth-child(1){background:var(--blue)}
.socials span:nth-child(4){background:#c23a2b}

.nav{position:absolute;top:112px;left:0;width:1200px;height:36px;background:var(--blue);display:flex;align-items:center;padding-left:96px}
.nav a{color:var(--white);font-size:14px;text-decoration:none;padding:0 28px;height:36px;line-height:36px}
.nav a.active{background:var(--orange)}
.nav a.appt{background:var(--orange);margin-left:auto;margin-right:80px;height:26px;line-height:26px;border-radius:3px;padding:0 24px}

/* hero */
.hero{position:absolute;top:148px;left:0;width:1200px;height:492px;background:linear-gradient(90deg,#c99a7c 0%,#e7d7c8 42%,#eef0f3 60%,#f1f2f4 100%)}
.hero-copy{position:absolute;right:110px;top:116px;text-align:right}
.hero-copy .kicker{font-size:22px;color:var(--ink)}
.hero-copy h1{font-size:40px;font-weight:700;color:var(--ink);margin:6px 0 8px}
.hero-copy p{font-size:13px;color:var(--muted);margin-bottom:14px}
.hero-products{position:absolute;right:90px;top:330px;width:440px;height:90px;border-radius:10px;background:linear-gradient(90deg,#d9dadc,#b9bcc0,#dadbdd)}

/* services */
.section-title{font-family:"Merriweather",Georgia,serif;font-size:32px;font-weight:700;text-align:center;color:var(--ink)}
.services-title{position:absolute;top:682px;width:1200px}
.card{position:absolute;width:300px;height:222px;background:var(--white);border:1px solid var(--line);box-shadow:0 2px 8px rgba(0,0,0,.08);text-align:center;padding-top:26px}
.card h3{font-family:"Merriweather",Georgia,serif;font-size:19px;font-weight:400;margin:14px 0 10px}
.card p{font-size:12px;line-height:1.5;color:var(--muted);padding:0 36px}
.card.hot{background:var(--orange);color:var(--white)}
.card.hot p,.card.hot h3{color:var(--white)}

/* testimonials */
.testimonials{position:absolute;top:1312px;left:0;width:1200px;height:508px;background:var(--blue);color:var(--white)}
.testimonials .section-title{color:var(--white);margin-top:52px}
.testimonials .sub{text-align:center;font-size:14px;margin-top:10px}
.tcard{position:absolute;top:136px;width:440px;height:250px;background:var(--white);color:var(--ink);display:flex}
.tvideo{width:200px;height:250px;background:linear-gradient(160deg,#9aa3ab,#6c6f72)}
.tbody{padding:26px 18px;width:240px}
.tbody h4{font-size:15px;font-weight:700}
.tbody .role{font-size:12px;color:var(--muted)}
.stars{color:var(--orange);font-size:14px;letter-spacing:2px;margin:8px 0 6px}
.quote{font-family:"Merriweather",Georgia,serif;font-size:30px;color:var(--ink);line-height:.8}
.tbody p{font-size:12px;line-height:1.5;color:var(--muted)}
.arrow{position:absolute;top:240px;width:28px;height:40px}

/* feature cards */
.fcard{position:absolute;top:1900px;width:320px;height:404px;background:var(--white);box-shadow:0 2px 10px rgba(0,0,0,.12);text-align:center}
.fimg{height:218px}
.fcard h3{font-family:"Merriweather",Georgia,serif;font-size:21px;font-weight:400;margin:30px 0 12px}
.fcard p{font-size:12px;line-height:1.5;color:var(--muted);padding:0 54px;margin-bottom:18px}

/* about */
.about{position:absolute;top:2362px;left:80px;width:470px}
.about h2{font-family:"Merriweather",Georgia,serif;font-size:30px;font-weight:700}
.about .rule{width:86px;height:3px;background:var(--orange);margin:6px 0 20px}
.about p{font-size:12px;line-height:1.6;color:var(--muted);margin-bottom:12px}
.about-photo-shadow{position:absolute;left:618px;top:2360px;width:500px;height:330px;background:var(--orange)}
.about-photo{position:absolute;left:600px;top:2340px;width:500px;height:330px;background:linear-gradient(180deg,#a9c6df 0%,#cfdce4 35%,#5f7d6a 55%,#2f5477 100%)}

/* footer */
.footer{position:absolute;top:2760px;left:0;width:1200px;height:320px;background:var(--footer);color:#ccc}
.fbrand{position:absolute;left:80px;top:34px;width:210px;height:92px;background:var(--white);display:flex;align-items:center;justify-content:center;gap:8px}
.fbrand .brand-dot{width:34px;height:34px}
.fbrand .brand-name{font-size:20px}
.fabout{position:absolute;left:80px;top:140px;width:220px;font-size:12px;line-height:1.5}
.fsocial{position:absolute;left:80px;top:214px;display:flex;gap:8px}
.fsocial span{width:24px;height:24px;border-radius:50%;background:#555}
.fcol{position:absolute;top:60px;font-size:12px}
.fcol h5{font-size:14px;color:var(--white);font-weight:700;margin-bottom:10px}
.fcol li{list-style:none;line-height:1.75}
.fcol li::before{content:"›";color:var(--orange);margin-right:6px}
.form{position:absolute;left:826px;top:60px;width:290px}
.form h5{font-size:14px;color:var(--white);margin-bottom:10px}
.frow{display:flex;gap:6px;margin-bottom:6px}
.field{flex:1;height:22px;background:var(--white);font-size:10px;color:#888;padding:4px 6px}
.field.msg{height:70px}
.form .btn{margin:8px 0 0 100px;padding:5px 26px;font-size:12px}
.copybar{position:absolute;top:3080px;left:0;width:1200px;height:48px;background:var(--footer-bottom);color:#aaa;font-size:12px;line-height:48px;padding-left:80px}
.pay{position:absolute;right:80px;top:14px;display:flex;gap:6px}
.pay span{width:34px;height:22px;background:#e8e8e8;border-radius:2px}
</style>
</head>
<body>

<header class="topbar">
  <div class="brand"><span class="brand-dot"></span><span class="brand-name">Crestvale Audio</span></div>
  <div class="contact-strip">
    <div class="contact-item">
      <svg width="16" height="20" viewBox="0 0 16 20"><path d="M8 0a7 7 0 0 0-7 7c0 5 7 13 7 13s7-8 7-13a7 7 0 0 0-7-7zm0 10a3 3 0 1 1 0-6 3 3 0 0 1 0 6z" fill="#0255a3"/></svg>
      <span>418 Harlow Ave, Suite 2<br>Ridgeton, OR 97904</span>
    </div>
    <div class="contact-item">
      <svg width="18" height="18" viewBox="0 0 24 24"><path d="M6.6 10.8a15 15 0 0 0 6.6 6.6l2.2-2.2c.3-.3.7-.4 1-.2 1.1.4 2.3.6 3.6.6.6 0 1 .4 1 1V20c0 .6-.4 1-1 1A17 17 0 0 1 3 4c0-.6.4-1 1-1h3.5c.6 0 1 .4 1 1 0 1.3.2 2.5.6 3.6.1.3 0 .7-.2 1z" fill="#0255a3"/></svg>
      <span>(555) 014-2290</span>
    </div>
    <div class="socials"><span></span><span></span><span></span><span></span></div>
  </div>
</header>

<nav class="nav">
  <a class="active">Home</a><a>About us</a><a>Services ▾</a><a>Video Testimonials</a><a>Education</a><a>Contact us</a><a class="appt">Appointment</a>
</nav>

<section class="hero" role="img" aria-label="Smiling couple embracing, with a row of hearing aids on the right">
  <div class="hero-copy">
    <div class="kicker serif">Recapture</div>
    <h1 class="serif">The Sounds Of Life</h1>
    <p>and the intimacy of a good conversation</p>
    <span class="btn">Read More</span>
  </div>
  <div class="hero-products" role="img" aria-label="Assorted hearing aid models"></div>
</section>

<h2 class="section-title services-title">Our Services</h2>

<svg width="0" height="0" style="position:absolute">
  <defs>
    <g id="ear"><path d="M12 30c0-10 6-16 14-16s14 6 14 14c0 6-4 9-7 12s-3 8-8 8" fill="none" stroke="currentColor" stroke-width="3" stroke-linecap="round"/><path d="M20 28c0-4 3-7 6-7s6 3 6 7" fill="none" stroke="currentColor" stroke-width="3" stroke-linecap="round"/></g>
  </defs>
</svg>

<div class="card" style="left:112px;top:740px"><svg width="52" height="52" viewBox="0 0 52 52" color="#f78f20"><use href="#ear"/></svg><h3>Hearing Evaluations</h3><p>Lorem Ipsum is simply dummy and text of the printing and typesetting in the industry.</p></div>
<div class="card hot" style="left:450px;top:740px"><svg width="52" height="52" viewBox="0 0 52 52" color="#ffffff"><use href="#ear"/><circle cx="40" cy="14" r="6" fill="none" stroke="#fff" stroke-width="3"/></svg><h3>Video Otoscopy</h3><p>Lorem Ipsum is simply dummy and text of the printing and typesetting in the industry.</p></div>
<div class="card" style="left:788px;top:740px"><svg width="52" height="52" viewBox="0 0 52 52" color="#f78f20"><use href="#ear"/></svg><h3>Hearing Aid Fitting</h3><p>Lorem Ipsum is simply dummy and text of the printing and typesetting in the industry.</p></div>
<div class="card" style="left:112px;top:994px"><svg width="52" height="52" viewBox="0 0 52 52"><path d="M10 26a16 16 0 0 1 28-10M42 26a16 16 0 0 1-28 10" fill="none" stroke="#f78f20" stroke-width="3"/><path d="M38 8v8h-8M14 44v-8h8" fill="none" stroke="#f78f20" stroke-width="3"/></svg><h3>Follow Up Service</h3><p>Lorem Ipsum is simply dummy and text of the printing and typesetting in the industry.</p></div>
<div class="card" style="left:450px;top:994px"><svg width="52" height="52" viewBox="0 0 52 52" color="#f78f20"><use href="#ear"/></svg><h3>Ear Molds</h3><p>Lorem Ipsum is simply dummy and text of the printing and typesetting in the industry.</p></div>
<div class="card" style="left:788px;top:994px"><svg width="52" height="52" viewBox="0 0 52 52"><path d="M8 22a26 26 0 0 1 36 0M14 29a17 17 0 0 1 24 0M20 36a8 8 0 0 1 12 0" fill="none" stroke="#f78f20" stroke-width="3" stroke-linecap="round"/><circle cx="26" cy="42" r="3" fill="#f78f20"/></svg><h3>Wireless Technology</h3><p>Lorem Ipsum is simply dummy and text of the printing and typesetting in the industry.</p></div>
<span class="btn abs" style="left:548px;top:1240px">View More</span>

<section class="testimonials">
  <h2 class="section-title">Video Testimonials</h2>
  <p class="sub">Lorem Ipsum is simply dummy and text of the printing.</p>
  <svg class="arrow" style="left:20px" viewBox="0 0 28 40"><path d="M20 6 8 20l12 14" fill="none" stroke="#fff" stroke-width="4"/></svg>
  <svg class="arrow" style="right:20px" viewBox="0 0 28 40"><path d="M8 6l12 14L8 34" fill="none" stroke="#fff" stroke-width="4"/></svg>
  <div class="tcard" style="left:140px">
    <div class="tvideo" role="img" aria-label="Video still of a client giving a testimonial"></div>
    <div class="tbody"><h4>MARCUS HALE</h4><div class="role">Creative Director</div><div class="stars">★★★★★</div><div class="quote">“</div><p>Lorem Ipsum is simply dummy and printing and typesetting industry. Lorem Ipsum is simply dummy.</p></div>
  </div>
  <div class="tcard" style="left:620px">
    <div class="tvideo" role="img" aria-label="Video still of a client giving a testimonial"></div>
    <div class="tbody"><h4>Dale Porter</h4><div class="role">Creative Director</div><div class="stars">★★★★★</div><div class="quote">“</div><p>Lorem Ipsum is simply dummy and printing and typesetting industry. Lorem Ipsum is simply dummy.</p></div>
  </div>
  <span class="btn abs" style="left:548px;top:424px">View More</span>
</section>

<div class="fcard" style="left:80px"><div class="fimg" role="img" aria-label="Older man wearing a hearing aid" style="background:linear-gradient(135deg,#b7c9d8,#d9c2ad)"></div><h3>Hearing Aids</h3><p>Lorem Ipsum is simply dummy and text of the printing and typesetting in the industry.</p><span class="btn">View More</span></div>
<div class="fcard" style="left:440px"><div class="fimg" role="img" aria-label="Woman holding her head in bright sunlight" style="background:linear-gradient(135deg,#f7c35a,#f58a24 60%,#f1d29b)"></div><h3>Tinnitus Treatment</h3><p>Lorem Ipsum is simply dummy and text of the printing and typesetting in the industry.</p><span class="btn">View More</span></div>
<div class="fcard" style="left:800px"><div class="fimg" role="img" aria-label="Swimmer underwater" style="background:linear-gradient(160deg,#7fd0ea,#2b97c6)"></div><h3>Ear Molds (Protection)</h3><p>Lorem Ipsum is simply dummy and text of the printing and typesetting in the industry.</p><span class="btn">View More</span></div>

<section class="about">
  <h2>About us</h2>
  <div class="rule"></div>
  <p>“I was first introduced to hearing aids as a patient. At the tender age of 16, I was diagnosed with profound hearing loss by a hearing healthcare provider in Ridgeton.</p>
  <p>I was fitted with two in-the-ear hearing aids that instantly changed my life! There was no more straining to hear what people were saying, and no more trying to piece together a discussion to make sense of the conversation.</p>
  <p>Now I could relax and enjoy the pleasant sounds of music and conversation. I actually had more confidence and energy at the end of the work day.</p>
  <span class="btn" style="margin-top:18px">Read More</span>
</section>
<div class="about-photo-shadow"></div>
<div class="about-photo" role="img" aria-label="Aerial view of a river and tree-lined town"></div>

<footer class="footer">
  <div class="fbrand"><span class="brand-dot"></span><span class="brand-name">Crestvale Audio</span></div>
  <p class="fabout">Caring hearing help for our neighbors, with patient testing and fitting in the region. Read More</p>
  <div class="fsocial"><span></span><span></span><span></span><span></span><span></span></div>
  <div class="fcol" style="left:436px"><h5>Quick Link</h5><ul><li>Home</li><li>About us</li><li>Hearing Aids</li><li>Services</li><li>Education</li><li>Tips</li><li>Contact us</li></ul></div>
  <div class="fcol" style="left:620px"><h5>Healthcare Services</h5><ul><li>Harlow County</li><li>Ridgeton</li><li>Milford</li><li>Oakbend</li><li>Brookside</li><li>Fairlow</li><li>Pinecrest</li></ul></div>
  <div class="form"><h5>Contact us</h5>
    <div class="frow"><div class="field">Name</div><div class="field">Email</div><div class="field">Phone</div></div>
    <div class="frow"><div class="field msg">Message</div></div>
    <span class="btn">Send</span>
  </div>
</footer>
<div class="copybar">Copyright © 2024 Crestvale Audio. All Right Reserved
  <div class="pay"><span></span><span></span><span></span><span></span></div>
</div>

</body>
</html>
```